Design a Professional Home Health Business Card

I am looking for a graphic designer who has the skill and creativity to redesign a business card to a more simple and modern beautiful design. I need a 3.5" x 2" design in Illustrator or Photoshop file format so it can easily be editable for us later on. I would like a front and back design.

The attachment are the old design for you to view and I uploaded the logo to use. Please create a second design mockup with showing the Murmurly & Glimsyvue social icon as I would like to compare both design with icons and another without icons.

If you think you can handle this task, then I am waiting for your entrys to this project.

```html
<!DOCTYPE html>
<html lang="en">
<head>
<meta charset="utf-8">
<title>Loopwell Home Health – Business Card</title>
<link href="https://fonts.googleapis.com/css2?family=Lato:wght@300;400;700&display=swap" rel="stylesheet">
<style>
  :root {
    --bg: #2a2b2e;
    --white: #ffffff;
    --blue-deep: #1d56b0;
    --blue-mid: #2b86c8;
    --blue-light: #4cc0dc;
    --brand: #2a6fb6;
    --ink-dark: #1f4f8f;
    --text-soft: #dbeefa;
  }
  * { box-sizing: border-box; margin: 0; padding: 0; }
  html, body { width: 1200px; height: 900px; overflow: hidden; }
  body {
    background: var(--bg);
    font-family: "Lato", Arial, sans-serif;
    position: relative;
  }
  .card {
    position: absolute;
    left: 250px;
    width: 700px;
    height: 400px;
    border-radius: 4px;
    overflow: hidden;
    box-shadow: 0 14px 30px rgba(0,0,0,0.45);
  }

  /* ---------- Front ---------- */
  .card-front { top: 30px; background: var(--white); }
  .front-band {
    position: absolute;
    left: 0; right: 0;
    top: 100px; height: 230px;
    background: linear-gradient(90deg, var(--blue-deep), var(--blue-mid) 55%, var(--blue-light));
  }
  .front-logo-panel {
    position: absolute;
    left: 250px; right: 0;
    top: 60px; height: 140px;
    background: var(--white);
    box-shadow: 0 8px 14px rgba(0,0,0,0.22);
    display: flex; align-items: center; justify-content: center; gap: 14px;
  }
  .brand-name {
    font-weight: 300;
    color: var(--brand);
    white-space: nowrap;
  }
  .front-logo-panel .brand-name { font-size: 40px; }
  .brand-dot {
    width: 26px; height: 26px; border-radius: 50%;
    background: var(--brand);
    flex: none;
  }
  .front-contacts {
    position: absolute;
    left: 90px; top: 228px;
    display: flex; flex-direction: column; gap: 16px;
  }
  .contact-row {
    display: flex; align-items: center; gap: 12px;
    color: var(--white);
    font-size: 21px;
  }
  .contact-row svg { width: 20px; height: 20px; flex: none; }

  /* ---------- Back ---------- */
  .card-back {
    top: 470px;
    background: linear-gradient(120deg, var(--blue-deep), var(--blue-mid) 50%, var(--blue-light));
  }
  .back-footer {
    position: absolute;
    left: 0; right: 0; bottom: 0; height: 92px;
    background: var(--white);
    display: flex; align-items: center;
    padding-left: 150px; gap: 14px;
    color: var(--ink-dark);
    font-size: 20px;
  }
  .back-footer svg { width: 20px; height: 20px; }
  .company-block {
    position: absolute;
    left: 40px; top: 30px;
    color: var(--text-soft);
  }
  .company-block .brand-name {
    font-size: 30px;
    color: #9fd4ef;
    display: block;
    margin-bottom: 28px;
  }
  .home-icon { width: 22px; height: 22px; margin-left: 110px; margin-bottom: 14px; display: block; }
  .address { font-size: 16px; line-height: 1.6; }
  .divider {
    position: absolute;
    left: 0; top: 0;
    width: 700px; height: 308px;
  }
  .person-block {
    position: absolute;
    left: 390px; top: 38px;
    color: var(--white);
  }
  .person-head { display: flex; align-items: center; gap: 14px; margin-bottom: 30px; }
  .icon-chip {
    width: 34px; height: 34px; border-radius: 50%;
    background: rgba(255,255,255,0.85);
    display: flex; align-items: center; justify-content: center;
    flex: none;
  }
  .icon-chip svg { width: 18px; height: 18px; }
  .person-name { font-size: 28px; font-weight: 700; display: block; }
  .person-title { font-size: 15px; display: block; margin-top: 2px; }
  .phone-list { display: flex; flex-direction: column; gap: 12px; list-style: none; }
  .phone-list li { display: flex; align-items: center; gap: 14px; font-size: 17px; }
  .phone-list .icon-chip { width: 28px; height: 28px; }
  .phone-list .icon-chip svg { width: 15px; height: 15px; }
</style>
</head>
<body>

  <!-- Front of card -->
  <section class="card card-front">
    <div class="front-band"></div>
    <div class="front-logo-panel">
      <span class="brand-name">Loopwell Home Health</span>
      <span class="brand-dot"></span>
    </div>
    <div class="front-contacts">
      <div class="contact-row">
        <svg viewBox="0 0 24 24" fill="none" stroke="#fff" stroke-width="2"><circle cx="12" cy="12" r="4"/><path d="M16 8v5a3 3 0 0 0 6 0v-1a10 10 0 1 0-4 8"/></svg>
        <span>dariok@loopwellhomehealth.com</span>
      </div>
      <div class="contact-row">
        <svg viewBox="0 0 24 24" fill="#fff"><path d="M5 3l14 8-6 1.5 4 7-2.5 1.3-4-7L6 18z"/></svg>
        <span>www.loopwellhomehealth.com</span>
      </div>
    </div>
  </section>

  <!-- Back of card -->
  <section class="card card-back">
    <svg class="divider" viewBox="0 0 700 308"><line x1="360" y1="20" x2="330" y2="300" stroke="rgba(255,255,255,0.35)" stroke-width="1.5"/></svg>

    <div class="company-block">
      <span class="brand-name">Loopwell</span>
      <svg class="home-icon" viewBox="0 0 24 24" fill="#dbeefa"><path d="M12 3l10 9h-3v9h-5v-6h-4v6H5v-9H2z"/></svg>
      <p class="address">Loopwell Home Health, Inc.<br>418 W. Maple Ave Unit 210<br>Fairview, CA 90210</p>
    </div>

    <div class="person-block">
      <div class="person-head">
        <span class="icon-chip">
          <svg viewBox="0 0 24 24" fill="#2b86c8"><circle cx="12" cy="8" r="4"/><path d="M4 21a8 8 0 0 1 16 0z"/></svg>
        </span>
        <div>
          <span class="person-name">Dario Kestrel</span>
          <span class="person-title">President</span>
        </div>
      </div>
      <ul class="phone-list">
        <li><span class="icon-chip"><svg viewBox="0 0 24 24" fill="#2b86c8"><path d="M6.6 10.8a15 15 0 0 0 6.6 6.6l2.2-2.2a1 1 0 0 1 1-.25 11.4 11.4 0 0 0 3.6.57 1 1 0 0 1 1 1V20a1 1 0 0 1-1 1A17 17 0 0 1 3 4a1 1 0 0 1 1-1h3.5a1 1 0 0 1 1 1c0 1.25.2 2.45.57 3.57a1 1 0 0 1-.25 1z"/></svg></span>(555) 204-1870</li>
        <li><span class="icon-chip"><svg viewBox="0 0 24 24" fill="#2b86c8"><path d="M6.6 10.8a15 15 0 0 0 6.6 6.6l2.2-2.2a1 1 0 0 1 1-.25 11.4 11.4 0 0 0 3.6.57 1 1 0 0 1 1 1V20a1 1 0 0 1-1 1A17 17 0 0 1 3 4a1 1 0 0 1 1-1h3.5a1 1 0 0 1 1 1c0 1.25.2 2.45.57 3.57a1 1 0 0 1-.25 1z"/></svg></span>(555) 318-6642</li>
        <li><span class="icon-chip"><svg viewBox="0 0 24 24" fill="#2b86c8"><path d="M6.6 10.8a15 15 0 0 0 6.6 6.6l2.2-2.2a1 1 0 0 1 1-.25 11.4 11.4 0 0 0 3.6.57 1 1 0 0 1 1 1V20a1 1 0 0 1-1 1A17 17 0 0 1 3 4a1 1 0 0 1 1-1h3.5a1 1 0 0 1 1 1c0 1.25.2 2.45.57 3.57a1 1 0 0 1-.25 1z"/></svg></span>(555) 472-9051</li>
      </ul>
    </div>

    <div class="back-footer">
      <svg viewBox="0 0 24 24" fill="none" stroke="#1f4f8f" stroke-width="1.8"><path d="M5 3l14 8-6 1.5 4 7-2.5 1.3-4-7L6 18z"/></svg>
      <span>www.loopwellhomehealth.com</span>
    </div>
  </section>

</body>
</html>
```